Business Card Design

www.tallowoodrise.com.au

Tallowood Rise Bed and Breakfast
A unique property with spectacular views situated in a peaceful quiet court surrounded by other quality homes. Set back from the street, this wonderful residence has plenty of space. The huge paved driveway has tonnes of off street parking

Relax in the beautifully landscaped lawn area with mature trees. The stunning balcony & deck is an ideal place to sit & watch the spectacular sunsets through the tree tops. Just wonderful!

The self-contained Bed and Breakfast has its own separate entrance door and consists of a large lounge/ kitchenette with sink & a separate bedroom. The bathroom has a glass shower screen, toilet & vanity unit.
If you are looking for your own piece of paradise in an ideal established setting with plenty of room then you must stay at Tallowood rise
This really is a slice of Heaven so come & stay!

- Established landscaped gardens & lawn areas
- paved driveway - loads of off street parking
- Splendid balcony with glorious views
- Close to shopping & transport

We welcome you to relax and unwind in the charm of our modern country feel bed and breakfast in the Northern Suburbs of Adelaide, offering privacy and relaxation, it is perfect for couples
This self-contained bed & breakfast will provide you with a “home away from home”, including breakfast provisions and all the comfort and modern conveniences you’d expect Tallowood Rise is perfect whether you’re on a holiday visit to Adelaide or here for business.
Enjoy the many activities Adelaide has to offer, we are positioned in the Northern Suburbs for you to easily travel to the Adelaide Hills or Barossa Wine region.
Tallowood Rise B & B is in a fantastic location for whatever you want to do on your visit to South Australia. Nestled within walking distance to the Marlow Creek or visit our world renowned wine regions. Of course, we can help and point you in the right direction.

Industry/Entity Type

Shopping

Contact Information for Business Card

3 Tallowood Court
Salisbury Heights SA 5109

Doug & Fiona Prestley
0455 316 974 or 0438 625 407
www.tallowoodrise.com.au
doug@tallowoodrise.com.au

```html
<!DOCTYPE html>
<html lang="en">
<head>
<meta charset="utf-8">
<title>Tallowood Rise Bed and Breakfast – Business Card</title>
<link href="https://fonts.googleapis.com/css2?family=Josefin+Sans:wght@300;400&display=swap" rel="stylesheet">
<style>
  :root {
    --backdrop: #3a302b;
    --card-mint: #e9f6f3;
    --ink: #2b2b2b;
    --ink-soft: #4a4a4a;
    --cover-light: #b9d3c6;
    --cover-deep: #7e9f52;
    --title-light: #f7f7f2;
    --room-a: #8a6047;
    --room-b: #c9ab92;
    --entry-a: #cfcbbf;
    --entry-b: #7d6b58;
    --deck-a: #a9a392;
    --deck-b: #b87a45;
  }
  * { box-sizing: border-box; margin: 0; padding: 0; }
  html, body { width: 1200px; height: 1000px; overflow: hidden; }
  body {
    background: var(--backdrop);
    font-family: "Josefin Sans", sans-serif;
    position: relative;
  }
  .card {
    position: absolute;
    left: 280px;
    width: 640px;
    height: 366px;
    overflow: hidden;
  }
  .card-contact { top: 104px; background: var(--card-mint); }
  .card-cover { top: 530px; }

  .photo { position: absolute; }
  .photo-bedroom {
    left: 36px; top: 66px; width: 150px; height: 86px;
    background: linear-gradient(135deg, var(--room-a), var(--room-b));
  }
  .photo-entrance {
    left: 56px; top: 180px; width: 122px; height: 134px;
    background: linear-gradient(180deg, var(--entry-a), var(--entry-b));
  }
  .photo-balcony {
    left: 500px; top: 28px; width: 122px; height: 72px;
    background: linear-gradient(135deg, var(--deck-a), var(--deck-b));
  }

  .host-block {
    position: absolute;
    left: 200px; top: 76px; width: 290px;
    text-align: center;
    color: var(--ink);
  }
  .host-names {
    font-weight: 400;
    font-size: 24px;
    line-height: 1.1;
    letter-spacing: 0.5px;
  }
  .host-role {
    font-weight: 300;
    font-size: 10px;
    letter-spacing: 2.5px;
    text-transform: uppercase;
    margin-top: 4px;
    color: var(--ink-soft);
  }
  .contact-lines,
  .address-lines {
    font-weight: 300;
    font-size: 12.5px;
    line-height: 1.5;
    letter-spacing: 0.7px;
    color: var(--ink-soft);
  }
  .contact-lines { margin-top: 34px; }
  .address-lines { margin-top: 20px; }

  .cover-photo {
    position: absolute; inset: 0;
    background: linear-gradient(180deg, var(--cover-light), var(--cover-deep));
  }
  .cover-title {
    position: absolute;
    right: 34px; bottom: 34px;
    text-align: right;
    color: var(--title-light);
    font-weight: 300;
  }
  .cover-name {
    font-size: 36px;
    letter-spacing: 4px;
    text-transform: uppercase;
    line-height: 1.1;
  }
  .cover-kind {
    font-size: 32px;
    letter-spacing: 1px;
    line-height: 1.1;
  }
</style>
</head>
<body>
  <section class="card card-contact">
    <div class="photo photo-bedroom" role="img" aria-label="Photo of the guest bedroom"></div>
    <div class="photo photo-entrance" role="img" aria-label="Photo of the private entrance with breakfast table"></div>
    <div class="photo photo-balcony" role="img" aria-label="Photo of the balcony deck with outdoor setting"></div>

    <div class="host-block">
      <h1 class="host-names">Doug &amp; Fiona<br>Prestley</h1>
      <p class="host-role">Your Hosts</p>
      <p class="contact-lines">
        0455 316 974 or 0438 625 407<br>
        doug@tallowoodrise.com.au<br>
        www.tallowoodrise.com.au
      </p>
      <p class="address-lines">
        Tallowood Rise Bed and Breakfast<br>
        3 Tallowood Court Salisbury Heights<br>
        SA 5109
      </p>
    </div>
  </section>

  <section class="card card-cover">
    <div class="cover-photo" role="img" aria-label="Photo of the garden lawn and trees with a view over the plains"></div>
    <div class="cover-title">
      <p class="cover-name">Tallowood Rise</p>
      <p class="cover-kind">Bed and Breakfast</p>
    </div>
  </section>
</body>
</html>
```